Threadlane: fashion design product software needs your help

Fashion design product software company requests your assistance in designing a complete stationary package around our new logo design. Our software assists fashion designers and apparel houses with efficient communication and streamlined production between each other and manufacturers throughout the entire project design life cycle.

The look should reflect clean, simple and modern design. Not too "techie." Must use the provided logo and colors (or variations on the chosen colors, i.e. percentages as needed).

Reference website: www.threadlane-example.com

Buzzwords: manufacturing, production, apparel design/ers, streamlined process, effective communication, business, production software.

Please try to tone down or make the colors more subtle with more simple design style, layout. No sewing  theme. Thank you.

Target Market(s)

fashion designers and apparel houses that use software to manage and track production process life cycle.

Industry/Entity Type

Communication

Requirements
Must have
• Use of the logo and colors-or variations of colors (attached)
Nice to have
• Playfulness but corporate: with a sense of practicality, economical, streamlined production. Embossing considered.
Should not have
• Please keep in mind economics both financially and economically. Save trees and money! We believe in tactile paper but not "fashion-y" or sparkly, over-the-top colors, effects or production.

```html
<!DOCTYPE html>
<html lang="en">
<head>
<meta charset="utf-8">
<title>Threadlane Letterhead</title>
<link href="https://fonts.googleapis.com/css2?family=Arimo:wght@400&display=swap" rel="stylesheet">
<style>
  :root {
    --stage: #000000;
    --paper: #ffffff;
    --brand-blue: #33aee2;
    --brand-blue-light: #7ccbed;
    --brand-brown: #6e3b2b;
    --ink: #333333;
    --muted: #8a5546;
  }
  * { margin: 0; padding: 0; box-sizing: border-box; }
  html, body {
    width: 1200px; height: 831px; overflow: hidden;
    background: var(--stage);
  }
  .canvas { position: relative; width: 1200px; height: 831px; }
  .sheet { position: absolute; top: 41px; width: 562px; height: 738px; }
  .letterhead { left: 28px; background: var(--paper); }
  .reverse { left: 609px; background: var(--brand-blue); }

  .company-name {
    position: absolute;
    font-family: "Arimo", Arial, sans-serif;
    font-weight: 400;
    white-space: nowrap;
  }
  .letterhead .company-name {
    right: 48px; top: 84px;
    font-size: 40px; line-height: 44px;
    color: var(--brand-brown);
  }
  .reverse .company-name {
    left: 0; right: 0; top: 305px;
    text-align: center;
    font-size: 72px; line-height: 84px;
    color: var(--brand-blue-light);
  }

  .letter {
    font-family: "Arimo", Arial, sans-serif;
    color: var(--ink);
    font-size: 7.6px; line-height: 10px;
  }
  .recipient { position: absolute; left: 48px; top: 142px; font-style: normal; }
  .sender {
    position: absolute; left: 400px; top: 145px; font-style: normal;
    color: var(--muted); font-size: 7px; line-height: 9.4px;
  }
  .sender .label { color: var(--brand-blue); display: inline-block; width: 9px; }
  .date { position: absolute; left: 48px; top: 244px; }
  .salutation { position: absolute; left: 48px; top: 264px; }
  .body { position: absolute; left: 48px; top: 300px; width: 480px; line-height: 10.8px; }
  .body p { margin-bottom: 8px; }
  .closing { position: absolute; left: 48px; top: 612px; }
  .signature {
    position: absolute; left: 48px; top: 632px;
    width: 66px; height: 38px; border-radius: 10px;
    background: linear-gradient(90deg, rgba(51,174,226,0.25), rgba(51,174,226,0.55));
  }
</style>
</head>
<body>
<div class="canvas">
  <section class="sheet letterhead letter">
    <div class="company-name">Threadlane</div>

    <address class="recipient">
      Marina Holt<br>14 Linden Row<br>Market Street<br>Eastfield<br>County KT4 2PL
    </address>

    <address class="sender">
      Threadlane Technologies Corp<br>
      210 Mercer Street<br>
      New York, NY 10012<br>
      <span class="label">T</span>555-013-4420<br>
      <span class="label">E</span>contact@threadlane-example.com<br>
      www.threadlane-example.com
    </address>

    <p class="date">18 September 2010</p>
    <p class="salutation">Dear Ms Holt</p>

    <div class="body">
      <p>Thank you for your interest in our production platform. This letter outlines how our tools help your studio share design files, track samples and keep every partner informed from first sketch through final delivery to stores.</p>
      <p>Each collection begins with a shared workspace where designers, pattern makers and buyers can review changes together and leave clear notes for the next step.</p>
      <p>Our scheduling view lists every style in production, its current stage and the supplier responsible for it. Delays are flagged early so your team can adjust orders before costs grow. Fabric, trim and label details stay attached to each style, which means factories always work from the latest approved specification and fewer samples need to be remade.</p>
      <p>Communication is the heart of a smooth season. Messages, approvals and comments are stored beside the garment they concern, so nobody has to search long email threads to find a decision. Suppliers receive only the information they need, in their own language where available, and can confirm dates, quantities and shipping details directly in the system. Managers see a simple summary of open tasks each morning, helping them focus on the items that matter most and keep collections on schedule across every market.</p>
      <p>We would be pleased to arrange a short demonstration for your team at a time that suits you. During the session we will walk through a sample collection, show how costings and timelines are updated, and answer any questions about setup, training and support. Most studios are fully running within two weeks, and our specialists remain available by phone and email whenever you need them. Pricing is based on the number of active styles, so you only pay for what you use as your business grows.</p>
      <p>Please contact us to book your demonstration. We look forward to helping your studio plan, produce and deliver each collection with less effort.</p>
    </div>

    <p class="closing">Kind regards</p>
    <div class="signature" role="img" aria-label="Handwritten signature in blue ink"></div>
  </section>

  <section class="sheet reverse">
    <div class="company-name">Threadlane</div>
  </section>
</div>
</body>
</html>
```